Brightwell-Joinery - DL Flyer - Kitchen Renovations & Cabinetry - Eye Catching Design

Please design a creative, professional DL flyer for us (DL Size: 98 x 210mmm), incorporating details outlined below...

Font: Helvetica Neue (same as logo)

Front: Main logo (01.eps) as a feature, website on the bottom (brightwell-joinery.com.au).

Back: Three key words to be featured: Kitchens I Benchtops I Custom Cabinetry
2-3 clear images showing our work (more have been provided so you can select the images that work the best with the design). We have also attached the icon from our logo on 4 x different colour backgrounds, which could be incorporated (on back).
Text to include: 'Servicing all areas, we come to you!'

Contact details: 'Call us now on 0461 872 309'. enquiries@brightwell-joinery.com.au Lic. No. BLD 738402

Look forward to seeing what you come up with.

Target Market(s)

Home owners, 35-80+ age bracket

Industry/Entity Type

Kitchen

Font styles to use
Other font styles liked:
• Helvetica Neue

Requirements
Must have
• Logo and website on front page of flyer. Minimum of 2-3 images incorporated. Contact details as per project description. Text on back page, 3 key words: Kitchens I Benchtops I Custom Cabinetry
• Creative, eye-catching design layout. Consistent theming with business card (see attached), including colours (grey, white, blues)
Nice to have
• Creative, eye-catching way to incorporate photos.
Should not have
• Not too busy/cluttered

```html
<!DOCTYPE html>
<html lang="en">
<head>
<meta charset="utf-8">
<title>Brightwell-Joinery DL Flyer</title>
<link rel="stylesheet" href="https://fonts.googleapis.com/css2?family=Arimo:wght@400;700&display=swap">
<style>
  :root {
    --page-bg: #ecebe8;
    --card-white: #ffffff;
    --charcoal: #5d5f62;
    --logo-grey: #58585b;
    --tag-grey: #8a8b8d;
    --url-grey: #4e4f52;
    --accent-blue: #4a90d9;
    --text-light: #ffffff;
  }
  * { box-sizing: border-box; margin: 0; padding: 0; }
  html, body {
    width: 1200px;
    height: 1116px;
    overflow: hidden;
    background: var(--page-bg);
    font-family: "Arimo", "Helvetica Neue", Helvetica, Arial, sans-serif;
  }
  .flyer-side {
    position: absolute;
    width: 901px;
    height: 420px;
  }
  .flyer-front {
    left: 122px;
    top: 99px;
    background: var(--card-white);
  }
  .brand-name {
    position: absolute;
    left: 0;
    right: 0;
    top: 148px;
    text-align: center;
    font-weight: 700;
    font-size: 52px;
    letter-spacing: 1px;
    color: var(--logo-grey);
  }
  .brand-tagline {
    position: absolute;
    left: 0;
    right: 0;
    top: 214px;
    text-align: center;
    font-size: 20px;
    letter-spacing: 8.6px;
    color: var(--tag-grey);
  }
  .front-url {
    position: absolute;
    left: 0;
    right: 0;
    top: 330px;
    text-align: center;
    font-size: 19px;
    color: var(--url-grey);
  }
  .flyer-back {
    left: 193px;
    top: 579px;
    background: var(--charcoal);
  }
  .service-keywords {
    position: absolute;
    left: 0;
    right: 0;
    top: 38px;
    text-align: center;
    font-size: 22px;
    color: var(--accent-blue);
  }
  .work-gallery {
    position: absolute;
    left: 0;
    top: 109px;
    width: 901px;
    height: 169px;
    display: flex;
    gap: 4px;
  }
  .work-photo { flex: 1; height: 100%; }
  .photo-bathroom { background: linear-gradient(135deg, #d9b9a2 0%, #c49a80 55%, #2d8c8a 100%); }
  .photo-benchtop { background: linear-gradient(180deg, #9a9ea2 0%, #d6d8d9 45%, #b9bcbe 100%); }
  .photo-study { background: linear-gradient(135deg, #b7a76a 0%, #e8dfae 50%, #8fb04a 100%); }
  .service-line {
    position: absolute;
    left: 0;
    right: 0;
    top: 318px;
    text-align: center;
    font-size: 19px;
    color: var(--text-light);
  }
  .contact-line {
    position: absolute;
    left: 0;
    right: 0;
    top: 363px;
    text-align: center;
    font-size: 13px;
    color: var(--text-light);
  }
</style>
</head>
<body>
  <section class="flyer-side flyer-front">
    <div class="brand-name">BRIGHTWELL-JOINERY</div>
    <div class="brand-tagline">CABINETRY SOLUTIONS FOR YOUR HOME</div>
    <div class="front-url">www.brightwell-joinery.com.au</div>
  </section>

  <section class="flyer-side flyer-back">
    <h2 class="service-keywords" style="font-weight:400">KITCHENS I BENCHTOPS I CUSTOM CABINETRY</h2>
    <div class="work-gallery">
      <div class="work-photo photo-bathroom" role="img" aria-label="Photo of a renovated bathroom vanity with teal towels"></div>
      <div class="work-photo photo-benchtop" role="img" aria-label="Photo of a stone kitchen benchtop with a sink and kettle"></div>
      <div class="work-photo photo-study" role="img" aria-label="Photo of a built-in home office desk with cabinetry"></div>
    </div>
    <p class="service-line">Servicing all areas, we come to you!</p>
    <p class="contact-line">Call us now on 0461 872 309 | enquiries@brightwell-joinery.com.au | Lic. No. BLD 738402</p>
  </section>
</body>
</html>
```